Business Card for Dental Office

Our office is in the Hillcrest section of San Diego, California which is a well-established area. Maybe the back can be a map of our office location

```html
<!DOCTYPE html>
<html lang="en">
<head>
<meta charset="utf-8">
<title>Crestline Dental – Business Card</title>
<link href="https://fonts.googleapis.com/css2?family=Montserrat:wght@400;500;700&display=swap" rel="stylesheet">
<style>
  :root {
    --stage: #050505;
    --card-dark: #2a2a2a;
    --card-light: #f6f4ef;
    --ink: #6b6b6b;
    --ink-soft: #8a8a8a;
    --mark-light: #a9a9a9;
    --rule: #b9b9b9;
  }
  * { box-sizing: border-box; margin: 0; padding: 0; }
  html, body {
    width: 1200px; height: 1000px; overflow: hidden;
    background: var(--stage);
    font-family: "Montserrat", sans-serif;
  }
  .stage {
    position: relative; width: 1200px; height: 1000px;
    display: flex; align-items: center; justify-content: center; gap: 50px;
  }
  .card {
    width: 520px; height: 300px; border-radius: 14px;
    position: relative; overflow: hidden;
  }
  .card--back {
    background: var(--card-dark);
    display: flex; align-items: center; justify-content: center;
  }
  .brand {
    display: flex; align-items: center; gap: 12px;
    font-weight: 500; letter-spacing: 0.04em;
  }
  .brand__dot {
    width: 14px; height: 14px; border-radius: 50%;
  }
  .card--back .brand { color: var(--mark-light); font-size: 30px; }
  .card--back .brand__dot { background: var(--mark-light); }

  .card--front {
    background: var(--card-light);
    padding: 0 34px;
  }
  .card--front .brand {
    position: absolute; left: 34px; top: 104px;
    color: var(--ink-soft); font-size: 21px; width: 200px; line-height: 1.2;
  }
  .card--front .brand__dot { background: var(--ink-soft); flex: none; }
  .divider {
    position: absolute; left: 258px; top: 58px;
    width: 1px; height: 150px; background: var(--rule);
  }
  .contact {
    position: absolute; left: 282px; top: 66px;
    color: var(--ink); font-size: 13px; line-height: 1.35;
  }
  .contact__name { font-weight: 700; font-size: 16px; letter-spacing: 0.02em; }
  .contact__role { font-size: 14px; margin-bottom: 12px; }
  .contact__address { margin-bottom: 8px; }
  .contact__line { display: flex; align-items: center; gap: 8px; }
  .contact__line svg { width: 11px; height: 11px; fill: var(--ink); flex: none; }
  .website {
    position: absolute; left: 40px; bottom: 34px;
    color: var(--ink-soft); font-size: 12px; letter-spacing: 0.32em;
  }
</style>
</head>
<body>
  <main class="stage">
    <section class="card card--back" aria-label="Card back">
      <div class="brand"><span class="brand__dot"></span>Crestline Dental</div>
    </section>

    <section class="card card--front" aria-label="Card front">
      <div class="brand"><span class="brand__dot"></span>Crestline Dental</div>
      <div class="divider"></div>
      <div class="contact">
        <p class="contact__name">LOREAM IPSUM</p>
        <p class="contact__role">Owner</p>
        <p class="contact__address">412 Alder St. San Diego<br>CA 92103, USA</p>
        <p class="contact__line">
          <svg viewBox="0 0 24 24" aria-hidden="true"><path d="M6.6 10.8a15.1 15.1 0 0 0 6.6 6.6l2.2-2.2a1 1 0 0 1 1-.25 11.4 11.4 0 0 0 3.6.57 1 1 0 0 1 1 1V20a1 1 0 0 1-1 1A17 17 0 0 1 3 4a1 1 0 0 1 1-1h3.5a1 1 0 0 1 1 1c0 1.25.2 2.45.57 3.57a1 1 0 0 1-.25 1z"/></svg>
          1 (619) 555-0142
        </p>
        <p class="contact__line">
          <svg viewBox="0 0 24 24" aria-hidden="true"><path d="M2 5h20v14H2z M2 5l10 8 10-8" /></svg>
          loremipsum@email.com
        </p>
      </div>
      <p class="website">WWW.YOURWEBSITE.COM</p>
    </section>
  </main>
</body>
</html>
```